Home Page and One Inside Page Needed for Engine Modify Site

Website that sells kits to modify and enhance your car engine performance. I don't like direction / design of current site at http://www.brolvatemotors.com.php53-17.ord1-1.sitepreviewhub.com/

I want something modern. Something that shows power and performance.

I need home page and one inside page.

Keep blues and blacks and unfortunately that is their logo we have to work with. But this site needs WOW factor.

YOU DO NOT HAVE PERMISSION TO WORK OR SPEAK TO CLIENT DIRECTLY AND MUST WORK THROUGH ME.

```html
<!DOCTYPE html>
<html lang="en">
<head>
<meta charset="utf-8">
<title>brolvatemotors – precision exhaust header modeling system</title>
<link href="https://fonts.googleapis.com/css2?family=PT+Sans:wght@400;700&display=swap" rel="stylesheet">
<style>
:root{
  --blue:#1f1ff2;
  --blue-deep:#1414c8;
  --link:#2323d6;
  --ink:#111;
  --dark:#1d1e25;
  --panel:#1b1c24;
  --light:#efefef;
  --grey:#6b6b6b;
  --foot-text:#8a8b92;
  --hero-text:#b4b4ff;
  --white:#fff;
}
*{margin:0;padding:0;box-sizing:border-box}
html,body{width:1006px;height:1200px;overflow:hidden;background:var(--white)}
body{position:relative;font-family:"PT Sans",sans-serif;color:var(--ink)}
.abs{position:absolute}
ul{list-style:none}

/* header */
.header{left:0;top:0;width:1006px;height:84px;background:var(--white)}
.header__bar{left:158px;top:0;width:181px;height:4px;background:#111}
.brand{left:157px;top:22px}
.brand__name{font-size:28px;font-weight:700;color:var(--blue);letter-spacing:-.3px;line-height:1}
.brand__tag{font-size:9px;color:#111;margin-top:3px;letter-spacing:.1px}
.nav{right:158px;top:35px;display:flex;align-items:center;font-size:11.5px}
.nav a{color:var(--link);text-decoration:none;padding:0 11px;border-left:1px solid #ccd;line-height:12px}
.nav a:first-child{border-left:0;color:#111}
.nav a:last-child{padding-right:0}

/* hero */
.hero{left:0;top:84px;width:1006px;height:340px;background:radial-gradient(ellipse at 72% 45%,#202020 0%,#0a0a0a 55%,#030303 100%)}
.hero__photo{left:158px;top:20px;width:392px;height:300px;border-radius:6px;
  background:
    radial-gradient(ellipse 38% 30% at 46% 56%,#e0741f 0%,#b4521a 45%,rgba(180,82,26,0) 100%),
    radial-gradient(ellipse 30% 22% at 35% 22%,#f2f3f5 0%,rgba(242,243,245,0) 100%),
    linear-gradient(160deg,#dfe1e5 0%,#9a9ca3 32%,#4a4b51 68%,#18181b 100%);
  box-shadow:0 0 40px rgba(0,0,0,.6)}
.hero__copy{left:610px;top:134px;width:240px;font-size:11.2px;line-height:13px;color:var(--hero-text);letter-spacing:-.15px}
.hero__btn{left:610px;top:207px;width:65px;height:22px;background:var(--blue);color:#fff;font-size:11px;font-weight:700;text-align:center;line-height:22px;border-radius:2px}
.hero__arrow{top:122px}

/* features */
.features{left:0;top:424px;width:1006px;height:219px;background:var(--light)}
.feature{top:24px;width:216px;text-align:center}
.feature__photo{width:216px;height:92px}
.feature__title{margin-top:15px;font-size:11.5px;color:var(--link);display:flex;justify-content:center;align-items:center;gap:6px}
.feature__text{margin-top:15px;font-size:10px;line-height:13px;color:var(--grey)}

/* blue band */
.band{left:0;top:643px;width:1006px;height:329px;background:var(--blue)}
.band__title{font-size:13px;color:#fff;letter-spacing:-.2px}
.pager{display:flex;gap:4px}
.pager span{width:12px;height:11px;background:var(--blue-deep);border:1px solid #3a3aff;display:flex;align-items:center;justify-content:center}
.divider{left:614px;top:20px;width:1px;height:290px;background:linear-gradient(#1f1ff2,#1010a8,#1f1ff2)}
.usecase{left:158px;top:43px;width:434px;height:131px;background:var(--panel)}
.usecase__photo{left:15px;top:16px;width:185px;height:102px;background:linear-gradient(135deg,#d8d8dc,#6c6e7a 55%,#23242c)}
.usecase__text{left:211px;top:19px;width:212px;font-size:9.6px;line-height:13px;color:#fff}
.cats{left:631px;top:50px;font-size:10px;color:#fff}
.cats li{display:flex;align-items:center;gap:9px;height:17.3px}
.cats__figure{left:735px;top:14px;width:88px;height:158px;border-radius:6px;background:linear-gradient(#2a2f44,#161a2b)}
.gallery__photo{top:209px;height:86px}
.news{left:632px;top:209px;width:215px;height:86px;background:var(--panel);padding:15px 10px 0 11px;font-size:9.8px;line-height:13px;color:#fff}

/* footer */
.footer{left:0;top:972px;width:1006px;height:180px;background:var(--dark)}
.footer h3{font-size:13px;font-weight:400;color:#fff;margin-bottom:7px}
.footer li,.footer p{font-size:10px;color:var(--foot-text)}
.foot-nav li{display:flex;gap:6px;align-items:center;height:18px}
.social li{display:flex;align-items:center;gap:14px;height:31px;padding-left:10px}
.social i{width:16px;height:16px;border-radius:50%;background:#3a3b44;display:block}
.contact p{line-height:14.5px}
.subscribe__input{width:185px;height:22px;border:1px solid #55565e;background:#1a1b21;font-size:9.5px;color:#66676e;padding:4px 7px;margin-top:2px}
.subscribe__btn{margin-top:9px;width:55px;height:20px;background:#f3f3f3;border-radius:2px;font-size:10px;color:#111;text-align:center;line-height:20px}
.copyright{left:159px;top:1159px;font-size:10px;color:#555}
</style>
</head>
<body>

<header class="header abs">
  <div class="header__bar abs"></div>
  <div class="brand abs">
    <div class="brand__name">brolvatemotors</div>
    <div class="brand__tag">precision exhaust header modeling system</div>
  </div>
  <nav class="nav abs">
    <a href="#">HOME</a><a href="#">ABOUT US</a><a href="#">PRODUCT</a><a href="#">RESOURCES</a><a href="#">HOW IT WORKS</a><a href="#">CONTACT US</a>
  </nav>
</header>

<section class="hero abs">
  <svg class="hero__arrow abs" style="left:76px" width="44" height="98" viewBox="0 0 44 98"><polyline points="42,1 2,49 42,97" fill="none" stroke="#777" stroke-width="1.5"/></svg>
  <div class="hero__photo abs" role="img" aria-label="Chrome and orange V8 engine with polished exhaust headers and fan"></div>
  <p class="hero__copy abs">Lorem Ipsum is simply dummy text of the printing and typesetting industry. Lorem Ipsum has been the industry's standard dummy text ever since the 1500s, when an unknown printer took a galley of type and survived not only five centuries,</p>
  <div class="hero__btn abs">MORE</div>
  <svg class="hero__arrow abs" style="left:882px" width="44" height="98" viewBox="0 0 44 98"><polyline points="2,1 42,49 2,97" fill="none" stroke="#777" stroke-width="1.5"/></svg>
</section>

<section class="features abs">
  <div class="feature abs" style="left:158px">
    <div class="feature__photo" role="img" aria-label="Mechanic working on a red car engine" style="background:linear-gradient(135deg,#3c4a66,#8a3a2c 55%,#c8c0b0)"></div>
    <div class="feature__title">SYSTEM FEATURES <svg width="7" height="11" viewBox="0 0 7 11"><polyline points="1,1 6,5.5 1,10" fill="none" stroke="#2323d6" stroke-width="1.4"/></svg></div>
    <p class="feature__text">Lorem Ipsum is simply dummy text of the printing and typesetting industry. Lorem Ipsum has been type and survived not only five centuries,</p>
  </div>
  <div class="feature abs" style="left:395px">
    <div class="feature__photo" role="img" aria-label="Close-up of bronze engine tubing" style="background:linear-gradient(135deg,#3a2414,#c79a6a 50%,#4a2c16)"></div>
    <div class="feature__title">HOW IT WORKS <svg width="7" height="11" viewBox="0 0 7 11"><polyline points="1,1 6,5.5 1,10" fill="none" stroke="#2323d6" stroke-width="1.4"/></svg></div>
    <p class="feature__text">Lorem Ipsum is simply dummy text of the printing and typesetting industry. Lorem Ipsum has been type and survived not only five centuries,</p>
  </div>
  <div class="feature abs" style="left:632px">
    <div class="feature__photo" role="img" aria-label="Chrome motorcycle exhaust pipes" style="background:linear-gradient(135deg,#1c1c1e,#b4b6bc 50%,#2a2a2e)"></div>
    <div class="feature__title">OUR GALLERY <svg width="7" height="11" viewBox="0 0 7 11"><polyline points="1,1 6,5.5 1,10" fill="none" stroke="#2323d6" stroke-width="1.4"/></svg></div>
    <p class="feature__text">Lorem Ipsum is simply dummy text of the printing and typesetting industry. Lorem Ipsum has been type and survived not only five centuries,</p>
  </div>
</section>

<section class="band abs">
  <h2 class="band__title abs" style="left:158px;top:18px">WHO IS USING IT?</h2>
  <div class="pager abs" style="left:565px;top:21px"><span><svg width="6" height="5"><path d="M5 2.5H1M2.5 1 1 2.5 2.5 4" stroke="#fff" fill="none" stroke-width=".8"/></svg></span><span><svg width="6" height="5"><path d="M1 2.5h4M3.5 1 5 2.5 3.5 4" stroke="#fff" fill="none" stroke-width=".8"/></svg></span></div>
  <div class="usecase abs">
    <div class="usecase__photo abs" role="img" aria-label="Underside of a white sports car with tuned exhaust system"></div>
    <p class="usecase__text abs">Lorem Ipsum is :<br>when an unknown printer took a galley of type and scrambled it to make a type specimen book. It has survived not only five centuries, but also the leap into electronic typesetting, remaining essentially unchanged. It was popularised in the 1960s with the release of Letterset sheets containing</p>
  </div>

  <div class="divider abs"></div>

  <h2 class="band__title abs" style="left:631px;top:18px">OUR CATEGORIES</h2>
  <ul class="cats abs">
    <li><svg width="11" height="7"><path d="M0 3.5h10M7 1l3 2.5L7 6" stroke="#fff" fill="none" stroke-width=".9"/></svg>1625 Series</li>
    <li><svg width="11" height="7"><path d="M0 3.5h10M7 1l3 2.5L7 6" stroke="#fff" fill="none" stroke-width=".9"/></svg>1750 Series</li>
    <li><svg width="11" height="7"><path d="M0 3.5h10M7 1l3 2.5L7 6" stroke="#fff" fill="none" stroke-width=".9"/></svg>2000 Series</li>
    <li><svg width="11" height="7"><path d="M0 3.5h10M7 1l3 2.5L7 6" stroke="#fff" fill="none" stroke-width=".9"/></svg>FAbrication tools</li>
    <li><svg width="11" height="7"><path d="M0 3.5h10M7 1l3 2.5L7 6" stroke="#fff" fill="none" stroke-width=".9"/></svg>Home</li>
    <li><svg width="11" height="7"><path d="M0 3.5h10M7 1l3 2.5L7 6" stroke="#fff" fill="none" stroke-width=".9"/></svg>pre-bent tubing</li>
    <li><svg width="11" height="7"><path d="M0 3.5h10M7 1l3 2.5L7 6" stroke="#fff" fill="none" stroke-width=".9"/></svg>Uncategorized</li>
  </ul>
  <div class="cats__figure abs" role="img" aria-label="Mechanic in navy overalls holding a wrench and red toolbox"></div>

  <h2 class="band__title abs" style="left:157px;top:188px">OUR GALLERY</h2>
  <div class="pager abs" style="left:565px;top:191px"><span><svg width="6" height="5"><path d="M5 2.5H1M2.5 1 1 2.5 2.5 4" stroke="#fff" fill="none" stroke-width=".8"/></svg></span><span><svg width="6" height="5"><path d="M1 2.5h4M3.5 1 5 2.5 3.5 4" stroke="#fff" fill="none" stroke-width=".8"/></svg></span></div>
  <div class="gallery__photo abs" style="left:158px;width:139px;background:linear-gradient(135deg,#e0e4ea,#2e3a4e 50%,#6a88aa)" role="img" aria-label="Blue engine bay with intake"></div>
  <div class="gallery__photo abs" style="left:307px;width:138px;background:linear-gradient(135deg,#c8c8c8,#3a3a3c 55%,#9a9a9a)" role="img" aria-label="Silver exhaust headers on an engine"></div>
  <div class="gallery__photo abs" style="left:453px;width:139px;background:linear-gradient(135deg,#5a5a4c,#b8a88a 45%,#151515)" role="img" aria-label="Hand working on an engine block"></div>

  <h2 class="band__title abs" style="left:631px;top:188px">LATEST NEWS</h2>
  <div class="pager abs" style="left:820px;top:191px"><span><svg width="6" height="5"><path d="M5 2.5H1M2.5 1 1 2.5 2.5 4" stroke="#fff" fill="none" stroke-width=".8"/></svg></span><span><svg width="6" height="5"><path d="M1 2.5h4M3.5 1 5 2.5 3.5 4" stroke="#fff" fill="none" stroke-width=".8"/></svg></span></div>
  <div class="news abs">17-7-2013 : Lorem Ipsum is simply dummy text of the printing and typesetting industry. Lorem Ipsum has been type and survived not only five centuries,</div>
</section>

<footer class="footer abs">
  <div class="abs" style="left:157px;top:29px">
    <h3>Navigation</h3>
    <ul class="foot-nav">
      <li><svg width="8" height="5"><path d="M0 2.5h7M5 .5l2 2-2 2" stroke="#ccc" fill="none" stroke-width=".8"/></svg>Home</li>
      <li><svg width="8" height="5"><path d="M0 2.5h7M5 .5l2 2-2 2" stroke="#ccc" fill="none" stroke-width=".8"/></svg>About Us</li>
      <li><svg width="8" height="5"><path d="M0 2.5h7M5 .5l2 2-2 2" stroke="#ccc" fill="none" stroke-width=".8"/></svg>Product</li>
      <li><svg width="8" height="5"><path d="M0 2.5h7M5 .5l2 2-2 2" stroke="#ccc" fill="none" stroke-width=".8"/></svg>Resources</li>
      <li><svg width="8" height="5"><path d="M0 2.5h7M5 .5l2 2-2 2" stroke="#ccc" fill="none" stroke-width=".8"/></svg>How It Works</li>
      <li><svg width="8" height="5"><path d="M0 2.5h7M5 .5l2 2-2 2" stroke="#ccc" fill="none" stroke-width=".8"/></svg>Contact Us</li>
    </ul>
  </div>
  <div class="abs" style="left:313px;top:29px">
    <h3>Connect with Us</h3>
    <ul class="social">
      <li><i></i>Friendpage</li>
      <li><i></i>Chirper</li>
      <li><i></i>ViewTube</li>
    </ul>
  </div>
  <div class="contact abs" style="left:475px;top:29px">
    <h3>Contact Address</h3>
    <p>48 Harlow Lane Austin,</p>
    <p>TX 78790</p>
    <p>Phone: (512) 555 0142</p>
    <p>Fax: (512) 555 0187</p>
    <p>M-F 9-6</p>
    <p>Email: info@brolvatemotors.com</p>
  </div>
  <div class="abs" style="left:663px;top:29px">
    <h3>Subscribe for News Letter</h3>
    <div class="subscribe__input">Your &nbsp;E-mail ID</div>
    <div class="subscribe__btn">Subscribe</div>
  </div>
</footer>

<p class="copyright abs">2013 © Allright Reserved by brolvatemotors</p>

</body>
</html>
```